Banner Design Childrens Sports

We are a Children Multi Sport Gym
We are looking to have 5 large stand up banners made for when we travel to events.
Template has been added in attachments. one banner per sport

They need to be Trendy and draw you in and show care our photos. They should read as a group.

We have many sports:

Rhythmic Gymnastics
Artistic Gymnastics
Acrobatics
Tumbling trampoline
Aerial silks
Kick boxing

Toddler programs in the mornings and weekend
18 months - 3yo

Target Market(s)

Parents, student athletes

Industry/Entity Type

Fitness

Font styles to use
Serif
Sans Serif
Decorative

Colors
ec1f27
6b449b
ffffff
000000
aaaaaa
5c5c5c

Requirements
Must have
• Fluid design between banners
• Our Photos
• Trendy Design
• Company Logo
• www.bolvexsport.com
• 555.214.3087
• 4 Banner Designs, Show casing our sports
• Must be vertical, will be based out of a stand.
• 1-Rhytmic Gymnastic
• 2- Kickboxing
• 3-Artistic Gymnastics/ Tumbling Trampoline
• 4-Silks
• Artistic Banner
• Main Photo - Artistic 4
• 3 additional smaller photos
• 1- artistic 9
• 2- artistic 1
• 3- artistic 7
• Kickboxing
• Main Photo - boxing 2
• 1- Kickboxing 4
• 2- boxing 1
• 3- Kickboxing 6
• Trampoline & Tumbling
• Main Photo - Tramp1
• 1- Tramp 2
• 2- Text box - Waiting for your picture here
• 3- Text box - Come Join our TEAM
• Silk Banner
• Main Photo - Silk 2
• 1- Silk 5
• 2- Silk 3
• 3- Silk 4
• Silk Banner
• Main Photo - Rhythmic11
• 1- Rhythmic8
• 2- Rhythmic9
• 3- Rhythmic1

```html
<!DOCTYPE html>
<html lang="en">
<head>
<meta charset="UTF-8">
<title>Bolvex Sport – Event Roll-up Banners</title>
<link rel="stylesheet" href="https://fonts.googleapis.com/css2?family=Questrial&family=Montserrat:wght@600&display=swap">
<style>
  :root{
    --kick:#e11d2a;
    --rhythmic:#6b449b;
    --artistic:#7dc242;
    --tramp:#1f6fba;
    --silks:#e2305c;
    --white:#ffffff;
    --ink:#1a1a1a;
    --grey:#5c5c5c;
    --stage:#d4d4d4;
  }
  *{margin:0;padding:0;box-sizing:border-box}
  html,body{width:1200px;height:575px;overflow:hidden}
  body{background:var(--stage);font-family:"Questrial",sans-serif;position:relative}

  .banner{position:absolute;top:22px;width:206px;height:530px;background:linear-gradient(#f4f4f4,#e4e4e4);overflow:hidden;--accent:var(--kick)}
  .banner--kick{left:25px;--accent:var(--kick)}
  .banner--rhythmic{left:261px;--accent:var(--rhythmic)}
  .banner--artistic{left:497px;--accent:var(--artistic)}
  .banner--tramp{left:733px;--accent:var(--tramp)}
  .banner--silks{left:969px;--accent:var(--silks)}

  .hero{position:absolute;left:0;top:0;width:206px;height:345px;box-shadow:inset 0 0 40px rgba(0,0,0,.35)}
  .banner--kick .hero{background:linear-gradient(100deg,#1e1b1a 0,#3a2a24 30%,#b4562a 48%,#e07a35 52%,#5a3426 66%,#201c1c 100%)}
  .banner--rhythmic .hero{background:linear-gradient(170deg,#5f6a5a 0,#9aa294 30%,#d6d8d0 55%,#b9ad92 80%,#9c8a68 100%)}
  .banner--artistic .hero{background:linear-gradient(180deg,#1a2218 0,#3a4630 35%,#8a7358 55%,#3e4a34 72%,#151b14 100%)}
  .banner--tramp .hero{background:linear-gradient(180deg,#7d9cbc 0,#dcc8b6 30%,#eee8e0 48%,#c8332f 66%,#a82a2a 80%,#e6e6e6 100%)}
  .banner--silks .hero{background:linear-gradient(100deg,#241a20 0,#5a1c26 30%,#b8303c 50%,#5a1c26 70%,#1e1618 100%)}

  .shapes{position:absolute;left:0;top:0;width:206px;height:345px}
  .shapes polygon{fill:var(--accent)}

  .brand{position:absolute;top:13px;right:12px;font-size:15px;color:var(--white);letter-spacing:1px}
  .brand--left{right:auto;left:12px}

  .intro{position:absolute;top:42px;left:12px;color:var(--white);text-transform:uppercase;font-size:9px;line-height:10px}
  .intro--right{left:auto;right:12px;text-align:right}
  .intro__big{display:block;font-size:22px;line-height:26px;margin-top:1px}

  .sport{position:absolute;left:12px;top:280px;color:var(--white);font-weight:400;font-size:14px;line-height:15px;text-transform:uppercase}
  .sport--right{left:auto;right:12px;text-align:right;top:272px}

  .register{position:absolute;left:63px;top:318px;width:80px;height:80px;border-radius:50%;background:var(--white);border:2px solid var(--accent);display:flex;flex-direction:column;align-items:center;justify-content:center;text-transform:uppercase;font-size:8.5px;color:var(--ink);line-height:10px}
  .register__now{color:var(--accent)}

  .contact{position:absolute;left:0;top:410px;width:206px;text-align:center;color:var(--ink)}
  .contact__web{font-size:6px}
  .contact__label{font-size:6px;margin-top:6px;text-transform:uppercase}
  .contact__phone{font-family:"Montserrat",sans-serif;font-weight:600;font-size:14px;color:var(--accent);margin-top:2px}

  .thumbs{position:absolute;left:6px;top:460px;display:flex;gap:4px}
  .thumb{width:62px;height:64px;border:2px solid var(--white);box-shadow:inset 0 0 14px rgba(0,0,0,.3)}
  .banner--kick .thumb{background:linear-gradient(150deg,#8a8070,#d8d2c8 55%,#a83030)}
  .banner--kick .thumb:nth-child(2){background:linear-gradient(150deg,#6c7d86,#b63a3a 60%,#3a5a8a)}
  .banner--kick .thumb:nth-child(3){background:linear-gradient(150deg,#2c2c2c,#a83030 60%,#3a3030)}
  .banner--rhythmic .thumb{background:linear-gradient(150deg,#c9c4bb,#8a8580 60%,#6e6a66)}
  .banner--rhythmic .thumb:nth-child(2){background:linear-gradient(150deg,#35464a,#6a7a78 60%,#8c9a98)}
  .banner--rhythmic .thumb:nth-child(3){background:linear-gradient(150deg,#b8b8c0,#f0ede8 60%,#d8d4cc)}
  .banner--artistic .thumb{background:linear-gradient(150deg,#4d6b8c,#c8a4a8 60%,#3a4a7a)}
  .banner--artistic .thumb:nth-child(2){background:linear-gradient(150deg,#e8e4e0,#d8a8b0 50%,#7a90b0)}
  .banner--artistic .thumb:nth-child(3){background:linear-gradient(150deg,#2a3040,#6d7d9a 60%,#2a3040)}
  .banner--silks .thumb{background:linear-gradient(150deg,#5a3a7a,#b02a3a 60%,#3a2a5a)}
  .banner--silks .thumb:nth-child(2){background:linear-gradient(150deg,#4a3a60,#c23040 60%,#5a3a7a)}
  .banner--silks .thumb:nth-child(3){background:linear-gradient(150deg,#8a6aa0,#b02030 60%,#6a4a8a)}

  .thumb--photo{background:linear-gradient(150deg,#dcdcdc,#9aa8c4 55%,#3a5a9a)}
  .thumb--note{background:var(--tramp);color:var(--white);font-family:"Montserrat",sans-serif;font-weight:600;font-size:8px;line-height:9px;padding:6px 5px;display:flex;align-items:center;justify-content:center;text-align:center;box-shadow:none}
</style>
</head>
<body>

<section class="banner banner--kick">
  <div class="hero" role="img" aria-label="Main photo: young boy in kickboxing gloves throwing a punch in the gym"></div>
  <svg class="shapes" viewBox="0 0 206 345" aria-hidden="true">
    <polygon points="0,0 206,0 206,25 0,95"/>
    <polygon points="0,232 206,318 206,345 0,345"/>
  </svg>
  <div class="brand">BOLVEX</div>
  <p class="intro">Training<br>From<br>Professional<span class="intro__big">Coaches</span></p>
  <h2 class="sport">Kickboxing</h2>
  <div class="register"><span>Registered</span><span class="register__now">Now</span></div>
  <div class="contact">
    <p class="contact__web">www.bolvexsport.com</p>
    <p class="contact__label">Call us:</p>
    <p class="contact__phone">555.214.3087</p>
  </div>
  <div class="thumbs">
    <div class="thumb" role="img" aria-label="Coach holding pads for a young kickboxer"></div>
    <div class="thumb" role="img" aria-label="Two children sparring in the ring"></div>
    <div class="thumb" role="img" aria-label="Child kickboxer training"></div>
  </div>
</section>

<section class="banner banner--rhythmic">
  <div class="hero" role="img" aria-label="Main photo: rhythmic gymnast in a high leg extension with a hoop"></div>
  <svg class="shapes" viewBox="0 0 206 345" aria-hidden="true">
    <polygon points="0,0 206,0 206,20 0,70"/>
    <polygon points="0,232 206,330 206,345 0,345"/>
  </svg>
  <div class="brand">BOLVEX</div>
  <p class="intro" style="top:48px">Training<br>From<br>Professional<span class="intro__big">Coaches</span></p>
  <h2 class="sport">Rhythmic<br>Gymnastic</h2>
  <div class="register"><span>Registered</span><span class="register__now">Now</span></div>
  <div class="contact">
    <p class="contact__web">www.bolvexsport.com</p>
    <p class="contact__label">Call us:</p>
    <p class="contact__phone">555.214.3087</p>
  </div>
  <div class="thumbs">
    <div class="thumb" role="img" aria-label="Gymnast posing with a hoop"></div>
    <div class="thumb" role="img" aria-label="Gymnast in a split on the floor"></div>
    <div class="thumb" role="img" aria-label="Gymnast leaping"></div>
  </div>
</section>

<section class="banner banner--artistic">
  <div class="hero" role="img" aria-label="Main photo: two young gymnasts sitting on the bar"></div>
  <svg class="shapes" viewBox="0 0 206 345" aria-hidden="true">
    <polygon points="0,0 206,0 0,65"/>
    <polygon points="206,228 206,345 0,345 0,332"/>
  </svg>
  <div class="brand brand--left">BOLVEX</div>
  <p class="intro intro--right" style="top:36px">Training<br>From<br>Professional<span class="intro__big">Coaches</span></p>
  <h2 class="sport sport--right">Artistic<br>Gymnastics</h2>
  <div class="register"><span>Registered</span><span class="register__now">Now</span></div>
  <div class="contact">
    <p class="contact__web">www.bolvexsport.com</p>
    <p class="contact__label">Call us:</p>
    <p class="contact__phone">555.214.3087</p>
  </div>
  <div class="thumbs">
    <div class="thumb" role="img" aria-label="Gymnast on the beam"></div>
    <div class="thumb" role="img" aria-label="Gymnast saluting after a routine"></div>
    <div class="thumb" role="img" aria-label="Gymnast in a handstand on the bars"></div>
  </div>
</section>

<section class="banner banner--tramp">
  <div class="hero" role="img" aria-label="Main photo: row of young boys in team uniform sitting on the trampoline edge"></div>
  <svg class="shapes" viewBox="0 0 206 345" aria-hidden="true">
    <polygon points="0,0 206,0 206,55 0,12"/>
    <polygon points="0,240 206,318 206,345 0,345"/>
  </svg>
  <div class="brand">BOLVEX</div>
  <h2 class="sport">Trampoline<br>&amp; Tumbling</h2>
  <div class="register"><span>Registered</span><span class="register__now">Now</span></div>
  <div class="contact">
    <p class="contact__web">www.bolvexsport.com</p>
    <p class="contact__label">Call us:</p>
    <p class="contact__phone">555.214.3087</p>
  </div>
  <div class="thumbs">
    <div class="thumb thumb--note">Waiting for your picture here</div>
    <div class="thumb thumb--photo" role="img" aria-label="Young gymnast standing on the trampoline"></div>
    <div class="thumb thumb--note">Come Join our TEAM</div>
  </div>
</section>

<section class="banner banner--silks">
  <div class="hero" role="img" aria-label="Main photo: aerialist hanging upside down in red silks"></div>
  <svg class="shapes" viewBox="0 0 206 345" aria-hidden="true">
    <polygon points="0,0 206,0 0,75"/>
    <polygon points="0,232 206,320 206,345 0,345"/>
  </svg>
  <div class="brand brand--left">BOLVEX</div>
  <h2 class="sport" style="top:290px">Silks</h2>
  <div class="register"><span>Registered</span><span class="register__now">Now</span></div>
  <div class="contact">
    <p class="contact__web">www.bolvexsport.com</p>
    <p class="contact__label">Call us:</p>
    <p class="contact__phone">555.214.3087</p>
  </div>
  <div class="thumbs">
    <div class="thumb" role="img" aria-label="Aerialist posing in the silks"></div>
    <div class="thumb" role="img" aria-label="Group of students on the aerial silks"></div>
    <div class="thumb" role="img" aria-label="Aerialist in a split on the silks"></div>
  </div>
</section>

</body>
</html>
```